One page company profile for exclusive wine import

Valtrenor is an importer of exclusive, rare wines into indonesia. We would like a stylish, classy, upmarket but professional one pager containing our company profile.

Please include the text we prepared (see must haves) and read through it to get a better understanding of what our company is doing

We would like the one pager to have a dark background, and contain a drawing or drawing-style picture related to wine and/or global import (see examples). We would like to have it in PDF as well as in a word-template so we can later produce translations and/or adaptations to the text.

Target Market(s)

The one pagers is directed to distributors and upmarket hotels and restaurants.

Requirements
Must have
• We would like the one pager to have a dark background, and contain a drawing or drawing-style picture related to wine and/or global import (see examples)
• Our logo (see files) on the one pager
• The following contact details: E-mail: info@valtrenor-example.eu
• Word template and PDF
• The following text:
• "Valtrenor brings rare, exceptional wines to the Indonesian market. We
• specialize in French and Italian wines that even in Europe are very hard
• to get by. We have an extensive network of big and small, famous and less
• known winemakers that reserve a portion of their production for us.
• Together with them, we supply the market with an excellent range of the
• absolute best European wines.
• We buy our products directly at the winemaker in France or Italy Through a
• licensed importer, the wines are brought to Indonesia by airfreight and
• stored in air-conditioned, optimal conditions, awaiting distribution to
• our customers. All of this ensured that the wine loses none of its quality
• during transport from the winemaker to the customer.
• We always look out for partners that are eager to distribute or retail.
• Our intentions working with them are always to work on a long term basis.
• With these intentions we see that both sides together have to engage
• themselves to succeed in sales and establishing brand recognition in the
• Indonesian market. Our philosophy is based on trust, responsibility,
• mutual respect and of course a love for great wine!
• We advise our clients on tasting, food pairing, storing and aging the wine
• and provide a technical datasheet with all our bottles. We pride ourselves
• in our customer service and are always available for any enquiry."
Should not have
• clichés like pictures of grapes, vineyards, barrels, etc... (stylised drawings are preferred and allowed)

```html
<!DOCTYPE html>
<html lang="en">
<head>
<meta charset="UTF-8">
<title>Valtrenor – Company Profile</title>
<link href="https://fonts.googleapis.com/css2?family=Cormorant+Garamond:wght@500&family=Open+Sans:wght@400;700&display=swap" rel="stylesheet">
<style>
  :root {
    --stage: #fb7068;
    --page: #141313;
    --page-glow: #2a2828;
    --gold: #c9a24a;
    --wine: #b3121b;
    --wine-deep: #5c0a0e;
    --ink-light: #e9e6e2;
  }
  html, body {
    margin: 0;
    width: 1200px;
    height: 1200px;
    overflow: hidden;
    background: var(--stage);
  }
  .stage {
    width: 1200px;
    height: 1200px;
    display: flex;
    align-items: center;
    justify-content: center;
  }
  .profile-page {
    position: relative;
    width: 820px;
    height: 1080px;
    background: radial-gradient(ellipse at 50% 35%, var(--page-glow) 0%, var(--page) 65%);
    box-sizing: border-box;
    padding: 90px 90px 60px;
    color: var(--ink-light);
  }
  .brand {
    display: flex;
    align-items: center;
    gap: 18px;
  }
  .brand-dot {
    width: 54px;
    height: 54px;
    border-radius: 50%;
    background: var(--wine);
  }
  .brand-name {
    font-family: "Open Sans", sans-serif;
    font-weight: 700;
    font-size: 48px;
    letter-spacing: 3px;
    color: var(--ink-light);
  }
  .hero-illustration {
    display: block;
    margin: 10px auto 0;
    width: 300px;
    height: 420px;
  }
  .headline {
    font-family: "Cormorant Garamond", serif;
    font-weight: 500;
    font-size: 34px;
    line-height: 1.2;
    color: var(--gold);
    text-align: center;
    margin: 34px 0 0;
  }
  .divider {
    display: block;
    margin: 14px auto 0;
    width: 560px;
    height: 30px;
  }
  .profile-text {
    font-family: "Open Sans", sans-serif;
    font-weight: 400;
    font-size: 11.5px;
    line-height: 1.6;
    text-align: center;
    margin: 12px 0 0;
  }
  .profile-text p { margin: 0 0 12px; }
</style>
</head>
<body>
<main class="stage">
  <article class="profile-page">
    <header class="brand">
      <span class="brand-dot"></span>
      <span class="brand-name">VALTRENOR</span>
    </header>

    <svg class="hero-illustration" viewBox="0 0 300 420" role="img" aria-label="Stylised illustration of a golden wine glass filled with red wine">
      <defs>
        <linearGradient id="glassTone" x1="0" y1="0" x2="0" y2="1">
          <stop offset="0" stop-color="#3a2a22"/>
          <stop offset="0.35" stop-color="#a8121a"/>
          <stop offset="0.7" stop-color="#b98a3a"/>
          <stop offset="1" stop-color="#7a5a22"/>
        </linearGradient>
      </defs>
      <rect x="0" y="0" width="300" height="420" rx="8" fill="url(#glassTone)" opacity="0.9"/>
    </svg>

    <h1 class="headline">Valtrenor brings rare, exceptional wines to the<br>Indonesian market.</h1>

    <svg class="divider" viewBox="0 0 560 30" aria-hidden="true">
      <path d="M10 26 Q280 -6 550 26" fill="none" stroke="var(--wine)" stroke-width="2"/>
    </svg>

    <section class="profile-text">
      <p>We specialize in French and Italian wines that even in Europe are very hard to get by. We have an extensive network of big and small, famous and less known winemakers that reserve a portion of their production for us. Together with them, we supply the market with an excellent range of the absolute best European wines.</p>
      <p>We buy our products directly at the winemaker in France or Italy. Through a licensed importer, the wines are brought to Indonesia by airfreight and stored in air-conditioned, optimal conditions, awaiting distribution to our customers. All of this ensures that the wine loses none of its quality during transport from the winemaker to the customer. We always look out for partners that are eager to distribute or retail. Our intentions working with them are always to work on a long term basis. With these intentions we see that both sides together have to engage themselves to succeed in sales and establishing brand recognition in the Indonesian market. Our philosophy is based on trust, responsibility, mutual respect and of course a love for great wine!</p>
      <p>We advise our clients on tasting, food pairing, storing and aging the wine and provide a technical datasheet with all our bottles. We pride ourselves in our customer service and are always available for any enquiry.</p>
    </section>
  </article>
</main>
</body>
</html>
```